Custom Real Estate Postcard for Buying Communities

We are a real estate company that owns/operates mobile home parks and want to send out a postcard to owners of these communities letting them know who our company is and let them know we want to buy their community. We are looking to create a postcard that introduces our company to the owner and also lets them know we want to buy their community - we are targeting older mom & pop type communities so we would like the postcard to have a home-y feel that makes the owner feel like our company will treat them fairly during the acquisition process
I have attached a few images from our communities that might look good on a postcard - you don't need to use all of them, I just included multiple so there are different options. please feel free to edit/enhance the images if needed.
Our company is Brightfield Residential Partners (BRP) and the logo is attached.
Text to be included somewhere on postcard: "We pride ourselves on active hands-on management in order to provide our residents quality communities at an affordable price.
BRP is a proven owner/operator and has the ability to purchase without any financing contingencies.
We provide a quick and easy closing. We do not retrade
Target Market(s)
Owners of Mobile Home Parks that BRP (our company) would like to acquire - small mom & pop owners that want to see that we aren't the big firm trying to come in and take over but a local company that will still treat the residents well
Industry/Entity Type
Real Estate
Colors
Designer to choose colors to be used in the design.
Requirements
Must have
- The BRP logo, at least one picture of a mobile home park from the attached pictures. And some version/form of the provided text. Info/contact section with website (www.brphomesites.com), email (info@brphomesites.com) and phone (555.284.7096)
- Something sort of call to action like: "We Want to Buy Your Community", "Ready to Sell?", "Interested in Selling?" etc.
Nice to have
- BRP Logo Colors, in addition to any other colors if designer thinks there are complimentary colors

```html
<!DOCTYPE html>
<html lang="en">
<head>
<meta charset="utf-8">
<title>Brightfield Residential Partners — Acquisition Postcard</title>
<link rel="stylesheet" href="https://fonts.googleapis.com/css2?family=Titillium+Web:ital,wght@0,400;0,600;0,700;1,400;1,600&family=Lobster&family=Montserrat:wght@700;800;900&family=Roboto+Condensed:wght@400;700&display=swap">
<style>
  :root {
    --page: #dcdcdc;
    --rust: #8a2e1c;
    --orange: #c8641f;
    --bronze: #9c7434;
    --bronze-dark: #7a5a26;
    --ink: #111111;
    --black-panel: #161616;
    --gold: #f6c51b;
    --white: #ffffff;
    --bar: #ececec;
    --text-dark: #1d1d1d;
    --text-light: #e6e6e6;
    --ring: #c9c9c9;
    --rule: #9a9a9a;
  }
  * { box-sizing: border-box; margin: 0; padding: 0; }
  html, body { width: 991px; height: 1200px; overflow: hidden; }
  body { background: var(--page); position: relative; font-family: "Titillium Web", sans-serif; }

  .postcard { position: absolute; left: 116px; width: 772px; height: 498px; background: var(--white); overflow: hidden; }
  .postcard--front { top: 74px; }
  .postcard--back { top: 613px; }

  .shape-layer { position: absolute; inset: 0; width: 100%; height: 100%; }

  .brand { position: absolute; display: flex; align-items: center; gap: 14px; }
  .brand__dot { width: 44px; height: 44px; border-radius: 50%; background: var(--rust); flex: none; }
  .brand__name { font-family: "Titillium Web", sans-serif; font-weight: 400; font-size: 20px; line-height: 22px; letter-spacing: 1.5px; text-transform: uppercase; }
  .postcard--front .brand { left: 40px; top: 36px; }
  .postcard--front .brand__name { color: var(--text-dark); }
  .postcard--back .brand { left: 78px; top: 24px; }
  .postcard--back .brand__name { color: var(--white); }

  .headline { position: absolute; left: 28px; top: 118px; width: 300px; text-align: left; font-weight: 400; }
  .headline__putting { font-family: "Montserrat", sans-serif; font-weight: 800; font-size: 46px; line-height: 46px; color: var(--white); letter-spacing: 1px; text-shadow: 1px 1px 0 #6b6b6b, -1px -1px 0 #8a8a8a, 2px 2px 3px rgba(0,0,0,0.35); }
  .headline__community { font-family: "Lobster", cursive; font-weight: 400; font-size: 46px; line-height: 46px; color: var(--gold); margin-top: -2px; }
  .headline__first { font-family: "Montserrat", sans-serif; font-weight: 900; font-size: 70px; line-height: 68px; color: #1c1c1c; letter-spacing: 1px; text-shadow: 1px 0 0 #e8e8e8, -1px 0 0 #e8e8e8, 0 1px 0 #e8e8e8, 0 -1px 0 #e8e8e8, 2px 3px 4px rgba(0,0,0,0.4); }
  .headline__rule { position: absolute; left: 28px; top: 289px; width: 302px; border-top: 1px dotted #e6d2a8; }
  .headline__sub { position: absolute; left: 28px; top: 290px; font-style: italic; font-size: 24px; color: var(--white); }

  .intro { position: absolute; left: 27px; top: 344px; width: 344px; font-style: italic; font-size: 10.4px; line-height: 15px; color: var(--text-light); }
  .intro__name { color: var(--gold); }

  .contact-item { position: absolute; display: flex; align-items: center; gap: 8px; font-family: "Roboto Condensed", sans-serif; color: var(--text-dark); }
  .contact-item__icon { width: 14px; height: 14px; border-radius: 50%; background: var(--rust); display: flex; align-items: center; justify-content: center; }
  .contact-item--phone { left: 24px; top: 460px; font-weight: 700; font-size: 24px; }
  .contact-item--phone .contact-item__icon { width: 18px; height: 18px; }
  .contact-item--email { left: 298px; top: 468px; font-size: 13.5px; }
  .contact-item--web { left: 560px; top: 468px; font-size: 13.5px; }

  .cta { position: absolute; left: 20px; width: 382px; text-align: center; }
  .cta__sell { top: 108px; font-family: "Montserrat", sans-serif; font-weight: 800; font-size: 50px; line-height: 52px; color: var(--white); letter-spacing: 1px; text-shadow: 1px 1px 0 #7a7a7a, -1px -1px 0 #9a9a9a, 2px 2px 3px rgba(0,0,0,0.5); }
  .cta__community { top: 154px; font-family: "Lobster", cursive; font-weight: 400; font-size: 40px; line-height: 44px; color: var(--gold); }
  .about-title { position: absolute; left: 20px; width: 382px; top: 202px; text-align: center; font-style: italic; font-weight: 400; font-size: 17px; color: var(--white); letter-spacing: 0.5px; }
  .about-rule { position: absolute; left: 46px; width: 334px; height: 1px; background: var(--orange); }
  .about-copy { position: absolute; left: 52px; top: 236px; width: 328px; font-style: italic; font-size: 9.2px; line-height: 11.5px; color: var(--text-light); text-align: justify; }
  .about-copy p + p { margin-top: 11px; }

  .photo-frame { position: absolute; border: 4px solid var(--white); }
  .back-contact { position: absolute; font-family: "Roboto Condensed", sans-serif; color: var(--white); }
  .back-contact--phone { left: 50px; font-weight: 700; font-size: 20px; top: 458px; }
  .back-contact--web { left: 232px; font-size: 14px; top: 464px; letter-spacing: 0.5px; }

  .stamp-box { position: absolute; left: 672px; top: 23px; width: 75px; height: 90px; border: 1px solid #a9a9a9; display: flex; align-items: center; justify-content: center; text-align: center; font-family: "Roboto Condensed", sans-serif; font-weight: 700; font-size: 10.5px; line-height: 14px; color: #333; }
  .address-line { position: absolute; left: 451px; width: 296px; height: 1px; background: var(--rule); }
</style>
</head>
<body>

<section class="postcard postcard--front">
  <svg class="shape-layer" viewBox="0 0 772 498" aria-hidden="true">
    <defs>
      <linearGradient id="parkAerial" x1="0" y1="0" x2="1" y2="1">
        <stop offset="0" stop-color="#3f6a2c"/>
        <stop offset="0.45" stop-color="#6c8d4a"/>
        <stop offset="0.75" stop-color="#8ea277"/>
        <stop offset="1" stop-color="#2f5426"/>
      </linearGradient>
      <linearGradient id="bronzePanel" x1="0" y1="0" x2="1" y2="1">
        <stop offset="0" stop-color="#a67b38"/>
        <stop offset="1" stop-color="#8a6429"/>
      </linearGradient>
      <linearGradient id="homePhotoA" x1="0" y1="0" x2="0" y2="1">
        <stop offset="0" stop-color="#7ea45a"/>
        <stop offset="0.5" stop-color="#c9bfa6"/>
        <stop offset="1" stop-color="#6f6f6a"/>
      </linearGradient>
      <linearGradient id="homePhotoB" x1="0" y1="0" x2="0" y2="1">
        <stop offset="0" stop-color="#6a9bd0"/>
        <stop offset="0.5" stop-color="#d9dde0"/>
        <stop offset="1" stop-color="#8a8a86"/>
      </linearGradient>
      <linearGradient id="darkBand" x1="0" y1="0" x2="0" y2="1">
        <stop offset="0" stop-color="#1b1b1b"/>
        <stop offset="1" stop-color="#0b0b0b"/>
      </linearGradient>
    </defs>
    <rect x="270" y="0" width="502" height="324" fill="url(#parkAerial)" role="img" aria-label="Aerial photo of a manufactured home community surrounded by trees"/>
    <polygon points="0,0 268,0 274,20 0,20" fill="var(--rust)"/>
    <polygon points="274,0 282,0 378,322 370,322" fill="var(--orange)"/>
    <polygon points="0,20 300,20 324,106 0,106" fill="var(--white)"/>
    <polygon points="0,106 324,106 374,322 0,322" fill="url(#bronzePanel)"/>
    <rect x="0" y="322" width="772" height="3" fill="var(--white)"/>
    <rect x="0" y="325" width="772" height="130" fill="url(#darkBand)"/>
    <rect x="392" y="340" width="1" height="100" fill="#3a3a3a"/>
    <rect x="0" y="455" width="772" height="43" fill="var(--bar)"/>
    <polygon points="250,455 274,455 264,498 240,498" fill="var(--white)"/>
    <polygon points="510,455 534,455 524,498 500,498" fill="var(--white)"/>
    <circle cx="495" cy="374" r="68" fill="var(--ring)"/>
    <circle cx="495" cy="374" r="62" fill="url(#homePhotoA)" role="img" aria-label="Photo of a single-wide manufactured home"/>
    <circle cx="658" cy="374" r="68" fill="var(--ring)"/>
    <circle cx="658" cy="374" r="62" fill="url(#homePhotoB)" role="img" aria-label="Photo of a community street with homes and a parked truck"/>
  </svg>

  <div class="brand">
    <span class="brand__dot"></span>
    <span class="brand__name">Brightfield<br>Residential<br>Partners</span>
  </div>

  <h1 class="headline">
    <div class="headline__putting">PUTTING</div>
    <div class="headline__community">Community</div>
    <div class="headline__first">FIRST</div>
  </h1>
  <div class="headline__rule"></div>
  <p class="headline__sub">Sell Your Community to BRP</p>

  <p class="intro"><span class="intro__name">Brightfield Residential Partners (BRP)</span> is among the fastest-growing companies in the Manufactured Housing Industry and is constantly looking for communities to acquire. BRP has significant capital resources and the ability to make acquisitions without financing contingencies. We offer a quick due diligence and closing time line and we do not retrade. Please contact us if you are interested in selling your community.</p>

  <div class="contact-item contact-item--phone">
    <span class="contact-item__icon">
      <svg width="10" height="10" viewBox="0 0 24 24" aria-hidden="true"><path fill="#fff" d="M6.6 10.8a15 15 0 0 0 6.6 6.6l2.2-2.2c.3-.3.7-.4 1-.2 1.1.4 2.3.6 3.6.6.6 0 1 .4 1 1V20c0 .6-.4 1-1 1A17 17 0 0 1 3 4c0-.6.4-1 1-1h3.5c.6 0 1 .4 1 1 0 1.2.2 2.4.6 3.6.1.3 0 .7-.2 1z"/></svg>
    </span>
    <span>555.284.7096</span>
  </div>
  <div class="contact-item contact-item--email">
    <span class="contact-item__icon">
      <svg width="8" height="8" viewBox="0 0 24 24" aria-hidden="true"><rect x="2" y="5" width="20" height="14" fill="#fff"/></svg>
    </span>
    <span>info@brphomesites.com</span>
  </div>
  <div class="contact-item contact-item--web">
    <span class="contact-item__icon">
      <svg width="8" height="8" viewBox="0 0 24 24" aria-hidden="true"><circle cx="12" cy="12" r="9" fill="none" stroke="#fff" stroke-width="3"/></svg>
    </span>
    <span>www.brphomesites.com</span>
  </div>
</section>

<section class="postcard postcard--back">
  <svg class="shape-layer" viewBox="0 0 772 498" aria-hidden="true">
    <defs>
      <linearGradient id="backPanel" x1="0" y1="0" x2="0" y2="1">
        <stop offset="0" stop-color="#141414"/>
        <stop offset="1" stop-color="#1e1e1e"/>
      </linearGradient>
      <linearGradient id="bronzeBand" x1="0" y1="0" x2="1" y2="0">
        <stop offset="0" stop-color="#8c6528"/>
        <stop offset="1" stop-color="#a57b3a"/>
      </linearGradient>
      <linearGradient id="homePhotoC" x1="0" y1="0" x2="0" y2="1">
        <stop offset="0" stop-color="#6f9a48"/>
        <stop offset="0.55" stop-color="#d7d6cf"/>
        <stop offset="1" stop-color="#6e8a3c"/>
      </linearGradient>
      <linearGradient id="homePhotoD" x1="0" y1="0" x2="0" y2="1">
        <stop offset="0" stop-color="#7fa7d6"/>
        <stop offset="0.55" stop-color="#c9ccd0"/>
        <stop offset="1" stop-color="#7b7a5c"/>
      </linearGradient>
    </defs>
    <rect x="20" y="0" width="382" height="11" fill="var(--rust)"/>
    <rect x="20" y="11" width="382" height="443" fill="url(#backPanel)"/>
    <rect x="0" y="454" width="414" height="45" fill="url(#bronzeBand)"/>
    <rect x="48" y="358" width="155" height="81" fill="url(#homePhotoC)" role="img" aria-label="Photo of a manufactured home with a green porch and yard"/>
    <rect x="219" y="358" width="155" height="81" fill="url(#homePhotoD)" role="img" aria-label="Photo of a manufactured home with a white covered porch"/>
  </svg>

  <div class="brand">
    <span class="brand__dot"></span>
    <span class="brand__name">Brightfield<br>Residential<br>Partners</span>
  </div>

  <h2 class="cta cta__sell">SELL YOUR</h2>
  <p class="cta cta__community">Community to brp</p>
  <h3 class="about-title">ABOUT OUR COMPANY</h3>
  <div class="about-rule" style="top:231px"></div>
  <div class="about-copy">
    <p>BRP specializes in the acquisition and stabilization of value-add manufactured housing communities. We are actively expanding and have bought and sold more than 50 communities during the past five years. BRP uses proactive, hands-on management combined with strategic infusion of capital in order to turn distressed "trailer parks" into safe and desirable "communities".</p>
    <p>Our common-sense, proactive management allows us to capture financial upside and maximize returns for our investors, while providing our residents quality communities at an affordable price.</p>
  </div>
  <div class="about-rule" style="top:344px"></div>

  <div class="photo-frame" style="left:44px;top:354px;width:163px;height:89px"></div>
  <div class="photo-frame" style="left:215px;top:354px;width:163px;height:89px"></div>

  <div class="back-contact back-contact--phone">555.284.7096</div>
  <div class="back-contact back-contact--web">www.brphomesites.com</div>

  <div class="stamp-box">STAMP<br>HERE</div>
  <div class="address-line" style="top:198px"></div>
  <div class="address-line" style="top:254px"></div>
  <div class="address-line" style="top:305px"></div>
  <div class="address-line" style="top:362px"></div>
</section>

</body>
</html>
```